Kestrel Behavioural Consultancy needs a colourful yet professional website

I am looking for a clean, colourful yet professional website that will appeal to schools and families looking for training and consultancy for children with and without special needs. The company is called Kestrel Behavioural Consultancy. I would be open to stock images being used and I attach my logo in the files below which should complement the design of the website. My strap line is 'achieve believe succeed' A website which offers similar services that I like the menu layout of is www.tovrendo.com. I would initially be looking at 7 main title links of: Home, About, Services, Team/Careers, Events, Links, Contact Us. The services title should have a drop down menu linking to Parents, Schools, Training, Professional Development, Supervision. Each page would contain fixed text with stock images where appropriate, bar the Events page where it may be laid out differently to display separate course events coming up. A contact us form would be required under the relevant tab. Ideas of formats, templates, logo etc are attached below. I look forward to reviewing designs!

Target Market(s)

Families and Schools

Industry/Entity Type

Education

Coding

Font styles to use
Sans Serif

Requirements
Must have
• Logo incorporated
• Easy to read font
• Easy to navigate
Should not have
• Ultra modern minimalist style
• Dark colours

```html
<!DOCTYPE html>
<html lang="en">
<head>
<meta charset="utf-8">
<title>Kestrel Behavioural Consultancy</title>
<link href="https://fonts.googleapis.com/css2?family=Roboto:wght@400;500&family=Open+Sans:wght@400;600&family=Raleway:wght@500;600&display=swap" rel="stylesheet">
<style>
:root{
  --red:#c4101d;
  --red-dark:#a00c16;
  --green:#9cc43a;
  --green-dark:#8ab12c;
  --pink:#d9838c;
  --brown:#5b4320;
  --blue:#8cc7f5;
  --text:#555;
  --muted:#888;
  --white:#fff;
}
*{box-sizing:border-box;margin:0;padding:0}
html,body{width:1200px;height:2341px;overflow:hidden;background:var(--white)}
body{position:relative;font-family:"Open Sans",sans-serif;color:var(--text)}
.abs{position:absolute}

/* hero */
.hero-bg{left:0;top:0;width:1200px;height:693px;
  background:linear-gradient(180deg,#cfe6f8 0%,#eaf4fb 38%,#ffffff 52%,#d8ecc0 60%,#9fd14a 72%,#7fbf2c 100%)}
.hero-photo{left:577px;top:240px;width:515px;height:453px;
  background:radial-gradient(ellipse at 50% 40%,#f1c7a8 0%,#e8a98a 30%,#6fa060 60%,#5a8a3d 100%);border-radius:8px 8px 0 0}
.contact-top{left:117px;top:82px;font-family:"Roboto",sans-serif}
.contact-top .row{display:flex;align-items:center;gap:10px;height:26px}
.contact-top .phone{font-size:20px;color:#333}
.contact-top .mail{font-size:14px;color:#333}
.logo{left:0;width:1200px;top:82px;text-align:center;font-family:"Roboto",sans-serif;font-weight:500;font-size:34px;color:var(--brown)}
.logo span{display:block;font-size:12px;color:var(--red);font-weight:500;margin-top:2px}
.search{left:825px;top:100px;width:242px;height:36px;border-bottom:1px solid #999;font-family:"Roboto",sans-serif;font-size:15px;color:#777;display:flex;align-items:center;justify-content:space-between}
.nav{left:117px;top:155px;width:964px;height:55px;background:linear-gradient(180deg,#d8141f,var(--red-dark));display:flex}
.nav a{color:var(--white);text-decoration:none;font-family:"Roboto",sans-serif;font-size:16px;display:flex;align-items:center;justify-content:center;border-right:1px solid rgba(255,255,255,.35);height:100%}
.hero-title{left:117px;top:330px;font-family:"Roboto",sans-serif;line-height:1.25}
.hero-title .l1{font-size:37px;color:var(--green)}
.hero-title .l2{font-size:37px;color:var(--red)}
.hero-text{left:117px;top:432px;width:420px;font-size:14px;line-height:23px;color:#444}
.btn-red{left:117px;top:490px;width:124px;height:36px;background:var(--pink);color:var(--white);font-family:"Roboto",sans-serif;font-size:13px;display:flex;align-items:center;justify-content:center;border-radius:2px}
.dots{left:120px;top:547px;display:flex;gap:6px}
.dots i{width:17px;height:17px;border-radius:50%;border:2px solid var(--white);background:var(--white)}
.dots i:first-child{background:transparent}

/* about */
.section-title{left:0;width:1200px;text-align:center;font-family:"Roboto",sans-serif;font-size:31px;color:var(--red)}
.about-text{left:160px;width:880px;top:796px;text-align:center;font-size:15px;line-height:24px;color:var(--muted)}
.service{width:212px;height:212px;border-radius:50%;top:897px;display:flex;flex-direction:column;align-items:center;justify-content:center;color:var(--white);font-family:"Roboto",sans-serif;font-size:19px;line-height:22px;text-align:center}
.service svg{margin-bottom:10px}
.s1{left:144px;background:var(--green)}
.s2{left:381px;background:var(--pink)}
.s3{left:619px;background:var(--brown)}
.s4{left:857px;background:var(--blue)}

/* team */
.team-photo{left:0;top:1151px;width:1200px;height:456px;
  background:linear-gradient(90deg,#c9a9a0 0%,#e6d5c8 30%,#f0c9a6 45%,#d9a37f 60%,#6d9ccb 80%,#3d78b8 100%)}
.team-panel{left:125px;top:1151px;width:380px;height:456px;background:rgba(255,250,240,.78)}
.team-title{left:125px;width:380px;top:1228px;text-align:center;font-family:"Roboto",sans-serif;font-size:28px;color:var(--brown)}
.team-lead{left:165px;width:300px;top:1279px;text-align:center;font-size:14px;line-height:22px;color:#333}
.team-text{left:165px;width:300px;top:1334px;text-align:center;font-size:13px;line-height:22px;color:var(--muted)}
.btn-green{left:242px;top:1442px;width:124px;height:40px;border-radius:20px;background:var(--green);color:var(--white);font-family:"Roboto",sans-serif;font-size:15px;display:flex;align-items:center;justify-content:center}
.team-curve{left:0;top:1540px}

/* events */
.events-title{left:0;width:1200px;top:1648px;display:flex;justify-content:center;align-items:center;gap:14px;font-family:"Roboto",sans-serif;font-size:29px;color:var(--brown)}
.card{top:1711px;width:292px;height:283px;border:1px solid #ddd;background:var(--white)}
.card .pic{height:150px}
.card h3{margin:24px 26px 6px;font-family:"Roboto",sans-serif;font-weight:400;font-size:18px;color:var(--red)}
.card p{margin:0 26px;font-size:12.5px;line-height:21px;color:#666}
.card .date{margin:4px 26px 0;font-size:12.5px;color:var(--green-dark);font-weight:600}
.c1{left:134px}.c2{left:452px}.c3{left:771px}
.c1 .pic{background:linear-gradient(135deg,#c44b3a,#e6b8a0 50%,#2d3e55)}
.c2 .pic{background:linear-gradient(135deg,#6d8e4a,#c9d8b0 50%,#5d7e9a)}
.c3 .pic{background:linear-gradient(135deg,#5fa7d6,#f0d0b0 50%,#9dc05a)}

/* footer */
.footer-wave{left:0;top:2040px}
.footer-bg{left:0;top:2120px;width:1200px;height:221px;background:var(--green)}
.footer-logo{left:137px;top:2190px;font-family:"Roboto",sans-serif;font-weight:500;font-size:38px;color:var(--white)}
.copyright{left:137px;top:2249px;font-size:12.5px;line-height:20px;color:var(--white)}
.footer-h{font-family:"Raleway",sans-serif;font-weight:600;font-size:20px;color:var(--white)}
.news-h{left:510px;top:2168px}
.news-input{left:510px;top:2207px;width:220px;height:37px;background:var(--white);font-size:11.5px;color:#777;display:flex;align-items:center;padding-left:12px}
.news-btn{left:743px;top:2207px;width:71px;height:37px;background:var(--red);color:var(--white);font-family:"Raleway",sans-serif;font-weight:600;font-size:13px;display:flex;align-items:center;justify-content:center}
.contact-h{left:905px;top:2168px}
.contact-info{left:905px;top:2203px;font-size:12.5px;line-height:20px;color:var(--white)}
.contact-info .row{display:flex;align-items:center;gap:8px;color:var(--red)}
</style>
</head>
<body>

<div class="abs hero-bg" role="img" aria-label="Illustrated sky with clouds over green rolling hills and trees"></div>
<div class="abs hero-photo" role="img" aria-label="Photo of four smiling children leaning together"></div>

<div class="abs contact-top">
  <div class="row phone">
    <svg width="18" height="18" viewBox="0 0 24 24"><path fill="#9cc43a" d="M6.6 10.8c1.4 2.8 3.8 5.1 6.6 6.6l2.2-2.2c.3-.3.7-.4 1-.2 1.1.4 2.3.6 3.6.6.6 0 1 .4 1 1V20c0 .6-.4 1-1 1C10.6 21 3 13.4 3 4c0-.6.4-1 1-1h3.5c.6 0 1 .4 1 1 0 1.3.2 2.5.6 3.6.1.3 0 .7-.2 1z"/></svg>
    800-555-0147
  </div>
  <div class="row mail">
    <svg width="18" height="14" viewBox="0 0 24 18"><rect width="24" height="18" rx="2" fill="#c4101d"/><path d="M1 2l11 8 11-8" stroke="#fff" stroke-width="2" fill="none"/></svg>
    info@kestrel-bc.com
  </div>
</div>

<div class="abs logo">Kestrel<span>Behavioural Consultancy</span></div>

<div class="abs search">Search..
  <svg width="20" height="20" viewBox="0 0 24 24"><circle cx="10" cy="10" r="7" stroke="#d9838c" stroke-width="3" fill="none"/><path d="M15 15l6 6" stroke="#d9838c" stroke-width="3"/></svg>
</div>

<nav class="abs nav">
  <a style="width:133px">HOME</a>
  <a style="width:116px">ABOUT</a>
  <a style="width:139px">SERVICES</a>
  <a style="width:189px">TEAM/CAREERS</a>
  <a style="width:121px">EVENTS</a>
  <a style="width:94px">LINKS</a>
  <a style="width:172px;border-right:none">CONTACT US</a>
</nav>

<div class="abs hero-title"><div class="l1">Welcome to Kestrel</div><div class="l2">Behavioural Consultancy</div></div>
<p class="abs hero-text">Cum sociis natoque penatibus et magnis dis parturient montes nascetur ridiculus mus In iaculis facilisis massa</p>
<div class="abs btn-red">READ MORE</div>
<div class="abs dots"><i></i><i></i><i></i><i></i></div>

<h2 class="abs section-title" style="top:743px">About Kestrel Behavioural Consultancy</h2>
<p class="abs about-text">venenatis nec euismod sit amet egestas placerat est Pellentesque habitant morbi tristique senectus et netus et malesuada fames ac turpis egestas Cras id elit Integer quis urna Ut ante enim dapibus malesuada</p>

<div class="abs service s1">
  <svg width="80" height="56" viewBox="0 0 80 56" fill="none" stroke="#fff" stroke-width="2"><circle cx="28" cy="8" r="6"/><path d="M20 54V20h16v34M28 36v18"/><circle cx="52" cy="22" r="5"/><path d="M46 54V32h12v22"/></svg>
  Parent<br>Sibling Training
</div>
<div class="abs service s2">
  <svg width="70" height="60" viewBox="0 0 70 60" fill="none" stroke="#fff" stroke-width="2"><path d="M12 58V10l8-8 8 8v48M12 22h16M12 34h16M12 46h16M28 22l36 34"/></svg>
  Group<br>Services
</div>
<div class="abs service s3">
  <svg width="84" height="60" viewBox="0 0 84 60" fill="none" stroke="#fff" stroke-width="2"><path d="M4 28L40 4l36 24M12 22v36h56V22M32 58V40h16v18M56 12V4h8v14"/></svg>
  In home Early<br>Intervention
</div>
<div class="abs service s4">
  <svg width="70" height="60" viewBox="0 0 70 60" fill="none" stroke="#fff" stroke-width="2"><rect x="2" y="2" width="26" height="16" rx="3"/><path d="M8 18l-2 6 8-6"/><circle cx="44" cy="20" r="9"/><path d="M26 58c0-12 8-20 18-20s18 8 18 20z"/></svg>
  Parents<br>Consultancy
</div>

<div class="abs team-photo" role="img" aria-label="Photo of two smiling girls drawing with coloured pencils in a classroom"></div>
<div class="abs team-panel"></div>
<h2 class="abs team-title">Team/Career</h2>
<p class="abs team-lead">Avenenatis nec euismod sit amet egestas placerat est Pellentesque habitant</p>
<p class="abs team-text">Tristique senectus et netus et malesuada fames ac turpis egestas Cras id elit Integer quis urna Ut ante enim dapibus malesuada fringilla eu condimentum quis tellus Aenean porttitor eros</p>
<div class="abs btn-green">Read More</div>
<svg class="abs team-curve" width="1200" height="70" viewBox="0 0 1200 70"><path d="M0 40Q600 110 1200 40V70H0z" fill="#fff"/></svg>

<div class="abs events-title">
  <svg width="30" height="30" viewBox="0 0 30 30"><circle cx="15" cy="15" r="12" fill="#9cc43a"/></svg>
  Latest Events
  <svg width="30" height="30" viewBox="0 0 30 30"><circle cx="15" cy="15" r="12" fill="#9cc43a"/></svg>
</div>

<article class="abs card c1">
  <div class="pic" role="img" aria-label="Photo of children in pirate costumes at a party"></div>
  <h3>Cras a ante vitae enim</h3>
  <p>iaculis aliquam Mauris nunc quam venenatis nec euismod sit amet egesta</p>
  <p class="date">05 April 2016</p>
</article>
<article class="abs card c2">
  <div class="pic" role="img" aria-label="Photo of children running outdoors in a park"></div>
  <h3>Cras a ante vitae enim</h3>
  <p>iaculis aliquam Mauris nunc quam venenatis nec euismod sit amet egesta</p>
  <p class="date">05 April 2016</p>
</article>
<article class="abs card c3">
  <div class="pic" role="img" aria-label="Photo of a group of happy children lying together"></div>
  <h3>Cras a ante vitae enim</h3>
  <p>iaculis aliquam Mauris nunc quam venenatis nec euismod sit amet egesta</p>
  <p class="date">05 April 2016</p>
</article>

<svg class="abs footer-wave" width="1200" height="90" viewBox="0 0 1200 90">
  <path d="M0 60Q300 -10 620 20T1200 40V90H0z" fill="#9cc43a"/>
  <path d="M560 18Q900 40 1200 30" stroke="#c4101d" stroke-width="4" fill="none"/>
</svg>
<footer>
  <div class="abs footer-bg"></div>
  <div class="abs footer-logo">Kestrel</div>
  <p class="abs copyright">Copyright © 2016 Kestrel Behavioural Consultancy<br>All Right Reserved</p>

  <h4 class="abs footer-h news-h">Newsletter Sign Up</h4>
  <div class="abs news-input">Enter Email Address</div>
  <div class="abs news-btn">Sign Up</div>

  <h4 class="abs footer-h contact-h">Contact Info</h4>
  <div class="abs contact-info">
    42 Larchfield Lane<br>Dunmore, DK7 3PT
    <div class="row" style="margin-top:6px">
      <svg width="11" height="11" viewBox="0 0 24 24"><path fill="#c4101d" d="M6.6 10.8c1.4 2.8 3.8 5.1 6.6 6.6l2.2-2.2c.3-.3.7-.4 1-.2 1.1.4 2.3.6 3.6.6.6 0 1 .4 1 1V20c0 .6-.4 1-1 1C10.6 21 3 13.4 3 4c0-.6.4-1 1-1h3.5c.6 0 1 .4 1 1 0 1.3.2 2.5.6 3.6.1.3 0 .7-.2 1z"/></svg>
      1-800-555-0193
    </div>
    <div class="row" style="margin-top:4px">
      <svg width="12" height="9" viewBox="0 0 24 18"><rect width="24" height="18" rx="2" fill="#c4101d"/><path d="M1 2l11 8 11-8" stroke="#9cc43a" stroke-width="2" fill="none"/></svg>
      hello@kestrel-bc.com
    </div>
  </div>
</footer>

</body>
</html>
```